Dean Hollis Business Card

In addition to my name design (file uploaded), black print on white card stock, e-mail address should be presented as a typical e-mail address, i.e., underlined and in blue ink, the card should include the following information:
Professor of Flight Systems Studies
Aviation Incident Review Consultant
Senior Certified Flight Training Lead

dhollis@vexmail.example
Cedar Point, Northland
(555) 318-5074

```html
<!DOCTYPE html>
<html lang="en">
<head>
<meta charset="utf-8">
<title>Dean Hollis Business Card</title>
<link rel="stylesheet" href="https://fonts.googleapis.com/css2?family=Arimo:wght@400;700&family=Oswald:wght@600&display=swap">
<style>
  :root {
    --page-bg: #e4e5ea;
    --card-bg: #ffffff;
    --card-border: #0d0d0d;
    --ink: #111111;
    --rule-blue: #3f86c8;
    --link-blue: #1a5fd0;
    --pattern-light: #ffffff;
    --pattern-tone: #eeeff1;
  }
  * { box-sizing: border-box; margin: 0; padding: 0; }
  html, body {
    width: 1200px;
    height: 928px;
    overflow: hidden;
    background: var(--page-bg);
    font-family: "Arimo", Arial, sans-serif;
    color: var(--ink);
  }
  .stage {
    position: relative;
    width: 1200px;
    height: 928px;
  }
  .card {
    position: absolute;
    top: 299px;
    width: 540px;
    height: 330px;
    background: var(--card-bg);
    border: 7px solid var(--card-border);
    overflow: hidden;
  }
  .card--front { left: 30px; }
  .card--back { left: 630px; }

  .plane-pattern {
    position: absolute;
    inset: 0;
    background: radial-gradient(circle at 55% 55%, var(--pattern-tone) 0%, var(--pattern-light) 70%);
  }

  .wordmark {
    position: absolute;
    left: 0;
    right: 0;
    text-align: center;
    font-family: "Oswald", "Arial Narrow", sans-serif;
    font-weight: 600;
    font-size: 54px;
    letter-spacing: 4px;
    line-height: 1;
    color: var(--ink);
  }
  .rule {
    position: absolute;
    height: 3px;
    background: var(--rule-blue);
  }

  .card--front .wordmark { top: 16px; }
  .card--front .rule { top: 80px; left: 22px; right: 18px; }

  .credentials {
    position: absolute;
    left: 26px;
    top: 130px;
  }
  .credentials__title { font-size: 19px; margin-bottom: 4px; }
  .credentials__line { font-size: 13.5px; line-height: 1.35; }

  .contact {
    position: absolute;
    left: 32px;
    top: 212px;
    font-size: 18px;
    line-height: 1.22;
    font-style: normal;
  }
  .contact__email {
    color: var(--link-blue);
    text-decoration: underline;
    text-underline-offset: 3px;
  }

  .card--back .rule { top: 54px; left: 0; right: 0; }
  .card--back .wordmark { top: 80px; }
</style>
</head>
<body>
<main class="stage">
  <section class="card card--front" aria-label="Business card front">
    <div class="plane-pattern" role="img" aria-label="Scattered grey airplane silhouettes across the card"></div>
    <div class="wordmark">DEAN HOLLIS</div>
    <div class="rule"></div>
    <div class="credentials">
      <p class="credentials__title">Professor of Flight Systems Studies</p>
      <p class="credentials__line">Aviation Incident Review Consultant</p>
      <p class="credentials__line">Senior Certified Flight Training Lead</p>
    </div>
    <address class="contact">
      <span class="contact__email">dhollis@vexmail.example</span><br>
      Cedar Point, Northland<br>
      (555) 318-5074
    </address>
  </section>

  <section class="card card--back" aria-label="Business card back">
    <div class="plane-pattern" role="img" aria-label="Scattered grey airplane silhouettes with one large airplane at centre"></div>
    <div class="rule"></div>
    <div class="wordmark">DEAN HOLLIS</div>
  </section>
</main>
</body>
</html>
```